Business Card Design Project

Use our current logo. Clean design.

Industry/Entity Type

Business

Requirements
Must have
• Marisela DUBRANCQ
M. Law
Managing Partner

Alpenvorsa AG
Kornhalmweg 214
CH-3097 Liebefeld

M. +41 79 412 56 27
T. +41 31 928 44 10
F. +41 31 928 44 19

m.dubrancq@alpenvorsa-example.com
www.alpenvorsa-example.com

```html
<!DOCTYPE html>
<html lang="en">
<head>
<meta charset="utf-8">
<title>Alpenvorsa AG – Business Card</title>
<link rel="stylesheet" href="https://fonts.googleapis.com/css2?family=Tenor+Sans&family=Roboto+Condensed:wght@400&display=swap">
<style>
  :root{
    --stage:#2a2a2c;
    --card:#ffffff;
    --brand-red:#ea1c24;
    --deep-red:#6e0005;
    --mid-red:#b8121a;
    --ink:#111111;
    --tile:#ededed;
    --text:#222222;
    --white:#ffffff;
  }
  *{box-sizing:border-box;margin:0;padding:0}
  html,body{width:1200px;height:900px;overflow:hidden}
  body{background:var(--stage);position:relative;font-family:"Roboto Condensed",Arial,sans-serif}

  .card{position:absolute;left:287px;width:625px;height:356px;background:var(--card)}
  .card--front{top:64px}
  .card--back{top:480px}

  /* Front */
  .identity{position:absolute;left:17px;top:16px;width:252px;height:323px;background:var(--brand-red);font-family:"Tenor Sans",Georgia,sans-serif}
  .identity__brand{position:absolute;left:28px;top:36px;font-size:30px;color:var(--ink);letter-spacing:1px}
  .identity__rule{position:absolute;left:14px;top:88px;width:186px;height:1.5px;background:var(--ink)}
  .identity__degree{position:absolute;left:12px;right:10px;top:240px;display:flex;align-items:flex-end;gap:4px;font-size:15px;color:var(--white)}
  .identity__degree::before{content:"";flex:1;height:1px;background:var(--white);margin-bottom:4px}
  .identity__name{position:absolute;left:12px;top:255px;font-size:22px;color:var(--ink);-webkit-text-stroke:.6px var(--ink);white-space:nowrap;letter-spacing:.2px}
  .identity__role{position:absolute;left:12px;right:10px;top:281px;display:flex;align-items:flex-start;gap:2px;font-size:15px;color:var(--white)}
  .identity__role::after{content:"";flex:1;height:1px;background:var(--white);margin-top:7px}

  .contacts{position:absolute;left:283px;top:16px;width:326px;height:323px;display:grid;grid-template-columns:158px 158px;grid-template-rows:repeat(3,102px);column-gap:10px;row-gap:8.5px}
  .contact{background:var(--tile);position:relative;padding:8px 8px}
  .contact__icon{position:absolute;left:8px;top:10px;width:36px;height:36px}
  .contact__text{position:absolute;left:8px;right:4px;bottom:9px;font-size:15.5px;line-height:18px;color:var(--text)}
  .contact__text--small{font-size:14px;line-height:17px}
  .contact__text--web{font-size:13.4px}

  /* Back */
  .reverse{position:absolute;left:20px;top:20px;right:20px;bottom:20px;background:radial-gradient(ellipse at 20% 20%,var(--brand-red) 0%,var(--mid-red) 45%,var(--deep-red) 100%)}
  .reverse__brand{position:absolute;left:205px;top:148px;font-family:"Tenor Sans",Georgia,sans-serif;font-size:36px;letter-spacing:4px;color:var(--white)}
  .reverse__rule{position:absolute;left:195px;top:200px;width:290px;height:1.5px;background:var(--white)}
</style>
</head>
<body>

<section class="card card--front" aria-label="Business card front">
  <div class="identity">
    <div class="identity__brand">Alpenvorsa</div>
    <div class="identity__rule"></div>
    <div class="identity__degree"><span>M. Law</span></div>
    <div class="identity__name">Marisela DUBRANCQ</div>
    <div class="identity__role"><span>Managing Partner</span></div>
  </div>

  <div class="contacts">
    <div class="contact">
      <svg class="contact__icon" viewBox="0 0 36 36" aria-hidden="true"><path d="M8 4c2-1 4-1 5 1l3 6c1 2 0 3-2 4l-1 1c1 4 4 8 7 10l1-1c1-2 3-2 4-1l5 4c1 1 1 3-1 5-2 2-5 3-8 1C12 28 6 19 5 11c0-3 1-6 3-7z" fill="#111"/></svg>
      <div class="contact__text">+41 31 928 44 10</div>
    </div>
    <div class="contact">
      <svg class="contact__icon" viewBox="0 0 36 36" aria-hidden="true"><rect x="1" y="8" width="34" height="22" fill="#111"/><path d="M3 10l15 12 15-12M3 28l11-9M33 28l-11-9" stroke="#ededed" stroke-width="1.8" fill="none"/></svg>
      <div class="contact__text contact__text--small">m.dubrancq@<br>alpenvorsa-example.com</div>
    </div>
    <div class="contact">
      <svg class="contact__icon" viewBox="0 0 36 36" aria-hidden="true"><rect x="4" y="1" width="16" height="33" rx="2" fill="#111"/><rect x="6.5" y="4" width="11" height="10" fill="#ededed"/><g fill="#ededed"><rect x="6.5" y="17" width="3" height="2"/><rect x="10.5" y="17" width="3" height="2"/><rect x="14.5" y="17" width="3" height="2"/><rect x="6.5" y="21" width="3" height="2"/><rect x="10.5" y="21" width="3" height="2"/><rect x="14.5" y="21" width="3" height="2"/><rect x="6.5" y="25" width="3" height="2"/><rect x="10.5" y="25" width="3" height="2"/><rect x="14.5" y="25" width="3" height="2"/></g></svg>
      <div class="contact__text">+41 79 412 56 27</div>
    </div>
    <div class="contact">
      <svg class="contact__icon" viewBox="0 0 36 36" aria-hidden="true"><circle cx="18" cy="18" r="14" fill="#fff" stroke="#111" stroke-width="2.5"/><g stroke="#111" stroke-width="1.4" fill="none"><ellipse cx="18" cy="18" rx="6" ry="14"/><path d="M4 18h28M6 11h24M6 25h24M18 4v28"/></g><path d="M2 22c6 10 26 8 33-4" stroke="#111" stroke-width="2.5" fill="none"/></svg>
      <div class="contact__text contact__text--web">www.alpenvorsa-example.com</div>
    </div>
    <div class="contact">
      <svg class="contact__icon" viewBox="0 0 36 36" aria-hidden="true"><rect x="10" y="1" width="16" height="15" fill="#fff" stroke="#111" stroke-width="1.6"/><path d="M13 5h10M13 8h10M13 11h10" stroke="#111" stroke-width="1.3"/><rect x="2" y="16" width="32" height="18" fill="#fff" stroke="#111" stroke-width="2"/><path d="M8 28c0-5 20-5 20 0h-5v-2h-10v2z" fill="#111"/></svg>
      <div class="contact__text">+41 31 928 44 19</div>
    </div>
    <div class="contact">
      <svg class="contact__icon" viewBox="0 0 36 36" aria-hidden="true"><path d="M14 1C7 1 3 6 3 12c0 8 11 22 11 22s11-14 11-22C25 6 21 1 14 1z" fill="#111"/><circle cx="14" cy="12" r="4" fill="#ededed"/></svg>
      <div class="contact__text">Kornhalmweg 214<br>CH-3097 Liebefeld</div>
    </div>
  </div>
</section>

<section class="card card--back" aria-label="Business card back">
  <div class="reverse">
    <div class="reverse__brand">ALPENVORSA</div>
    <div class="reverse__rule"></div>
  </div>
</section>

</body>
</html>
```